依頼詳細
①主タイトル:朝霧草原
②全体のデザインスタイル:約やかで、モダン、馴染みやすい感じ。
栄養バランスが良い、食材が安全であること、
信頼感があり、ペットに安心して与えられること
を表現したい。
③セールスポイント:●生肉使用(食いつきが良い)
●穀物不使用(お腹と皮膚の健康ケア)
④犬のアウトラインが必要。(手書きの犬、犬の絵でも良い、実物写真は好ましくない)
⑤一部の原材料(牛肉、鶏肉、生サーモン、チーズ)を絵または写真で表現する。
⑥添付ファイルの主logoを入れてください。
記載項目
内容量は2kgです。
希望イメージ
シンプル 複雑
単色 カラフル
暗い 明るい
日常 高級
遊び心 厳粛
未来的 伝統的
女性的 男性的
希望する色
納品ファイル
補足説明
今回は犬用飼料のパッケージデザインを依頼させて頂きました。選定が決まりましたら、そのデザイナー様に続けて猫用飼料のパッケージデザインもお願いしたいと思っております。是非ともよろしくお願いいたします。
訂正です。内容量は2.5kgです。よろしくお願いいたします。

一目惚れでした。とてもインパクトがあります。

沢山のご提案ありがとうございました。
他にも好きなデザインがあったのですが、
今回の商品に一番合うデザインを選びました。
また機会があれば是非ともよろしくお願い致します。

```html
<!DOCTYPE html>
<html lang="ja">
<head>
<meta charset="utf-8">
<title>朝霧草原 ドッグフード</title>
<link href="https://fonts.googleapis.com/css2?family=Noto+Sans+JP:wght@500;700;900&family=Noto+Serif+JP:wght@700;900&family=Montserrat:wght@800&display=swap" rel="stylesheet">
<style>
  :root {
    --yellow: #f3c52f;
    --white: #ffffff;
    --ink: #1a1a1a;
    --title-red: #d4471c;
    --title-orange: #ef7a22;
    --star: #e8772a;
    --badge-red: #d8222b;
    --brand-green: #3c9a3f;
    --dog-tan: #e6a65a;
    --dog-dark: #6b4a2e;
  }
  html, body { margin: 0; padding: 0; overflow: hidden; }
  body { width: 799px; height: 1200px; background: var(--yellow); position: relative; font-family: "Noto Sans JP", sans-serif; color: var(--ink); }
  p { margin: 0; }
  .package { position: absolute; inset: 0; }
  .tagline { position: absolute; top: 56px; left: 0; width: 100%; text-align: center; font-weight: 700; font-size: 30px; line-height: 40px; color: var(--white); letter-spacing: 2px; }
  .corner-dog { position: absolute; border-radius: 40% 40% 12px 12px; }
  .corner-dog--left { left: 36px; top: 40px; width: 120px; height: 150px; background: linear-gradient(#fff8e8, #e7c089); }
  .corner-dog--right { right: 32px; top: 52px; width: 120px; height: 140px; background: linear-gradient(#f7e0b8, #d99a4f); }
  .panel { position: absolute; left: 0; top: 0; width: 799px; height: 1200px; }
  .reading { position: absolute; top: 238px; left: 0; width: 100%; text-align: center; font-family: "Noto Serif JP", serif; font-style: italic; font-weight: 700; font-size: 32px; line-height: 44px; letter-spacing: 3px; }
  .title { position: absolute; top: 300px; left: 0; width: 100%; text-align: center; margin: 0; font-family: "Noto Serif JP", serif; font-weight: 900; font-size: 118px; line-height: 130px; letter-spacing: 8px; color: var(--title-red); background: linear-gradient(var(--title-orange), var(--title-red)); -webkit-background-clip: text; background-clip: text; -webkit-text-fill-color: transparent; }
  .ingredients { position: absolute; top: 448px; left: 0; width: 100%; text-align: center; font-weight: 900; font-size: 30px; line-height: 40px; letter-spacing: 1px; }
  .badge { position: absolute; left: 572px; top: 500px; width: 196px; height: 196px; box-sizing: border-box; border-radius: 50%; background: var(--white); border: 4px solid var(--badge-red); text-align: center; color: var(--badge-red); }
  .badge__lead { display: block; margin-top: 26px; font-weight: 700; font-size: 16px; line-height: 22px; }
  .badge__main { display: block; margin: 6px auto 0; width: 150px; background: var(--badge-red); color: var(--white); font-weight: 900; font-size: 30px; line-height: 46px; border-radius: 6px; }
  .badge__note { display: block; margin-top: 8px; font-weight: 700; font-size: 13px; color: var(--ink); line-height: 19px; }
  .dogs { position: absolute; left: 70px; top: 520px; width: 480px; height: 510px; border-radius: 50% 50% 20px 20px; background: radial-gradient(circle at 50% 40%, var(--dog-tan), var(--dog-dark) 140%); }
  .pug { position: absolute; left: 565px; top: 720px; width: 165px; height: 310px; border-radius: 45% 45% 16px 16px; background: linear-gradient(#efe3cb, #c9b089); }
  .product-type { position: absolute; left: 40px; top: 1085px; }
  .product-type__name { font-family: "Montserrat", sans-serif; font-weight: 800; font-size: 40px; line-height: 44px; }
  .product-type__sub { font-size: 15px; font-weight: 500; }
  .brand { position: absolute; left: 330px; top: 1078px; display: flex; align-items: center; gap: 10px; }
  .brand__dot { width: 64px; height: 64px; border-radius: 50%; background: var(--brand-green); }
  .brand__name { font-weight: 700; font-size: 24px; color: var(--brand-green); }
  .weight { position: absolute; right: 40px; top: 1080px; font-family: "Noto Serif JP", serif; font-weight: 900; font-size: 56px; }
</style>
</head>
<body>
<main class="package">
  <p class="tagline">安全で栄養バランスが良い</p>
  <div class="corner-dog corner-dog--left" role="img" aria-label="白い犬のイラスト"></div>
  <div class="corner-dog corner-dog--right" role="img" aria-label="コーギー犬のイラスト"></div>

  <svg class="panel" viewBox="0 0 799 1200" aria-hidden="true">
    <path d="M60 1050 V215 H255 Q275 160 400 155 Q525 160 545 215 H740 V1050 Z" fill="#ffffff" stroke="#1a1a1a" stroke-width="4"/>
    <g fill="#e8772a">
      <polygon points="340,185 346,200 362,200 349,209 354,224 340,215 326,224 331,209 318,200 334,200"/>
      <polygon points="400,175 407,192 425,192 411,203 416,220 400,210 384,220 389,203 375,192 393,192"/>
      <polygon points="460,185 466,200 482,200 469,209 474,224 460,215 446,224 451,209 438,200 454,200"/>
    </g>
    <rect x="80" y="292" width="640" height="146" fill="none" stroke="#1a1a1a" stroke-width="4"/>
    <rect x="90" y="302" width="620" height="126" fill="none" stroke="#1a1a1a" stroke-width="1.5"/>
  </svg>

  <p class="reading">あさぎりそうげん</p>
  <h1 class="title">朝霧草原</h1>
  <p class="ingredients">牛肉・鶏肉・生サーモン・チーズ配合</p>

  <div class="dogs" role="img" aria-label="シェパードとゴールデンレトリバーのイラスト"></div>
  <div class="pug" role="img" aria-label="パグのイラスト"></div>

  <div class="badge">
    <span class="badge__lead">食べっぷりが違う!!</span>
    <span class="badge__main">生肉使用</span>
    <span class="badge__note">穀物不使用<br>お腹と皮膚の健康ケア</span>
  </div>

  <div class="product-type">
    <div class="product-type__name">Dog food</div>
    <div class="product-type__sub">to protect the health of pets</div>
  </div>
  <div class="brand"><span class="brand__dot"></span><span class="brand__name">Kibi Paws</span></div>
  <div class="weight">2.5kg</div>
</main>
</body>
</html>
```